Brimwell Lane Facebook Group Banner for a Little Girl's Boutique Retail/Wholesale Company

We need a Banner Designed for our facebook group. The previous one looks unprofessional and made at home.

Here is the information:
The size of the banner is 801X250.
Company Name: Brimwell Lane Buy Group

Overall Theme: Want to include crosses somehow, make it girly, flowers, vintage, professional

We need all of the same information on there. I attached a picture of the previous banner. We don’t like it at all so don’t use it as inspiration.
Information:
Private Message: Morwen Pike (best way to contact) <- please make “(best way to contact)” small
Email: morwenpike@brimwelllane.com
Emails and private messages are answered weekdays 8am to 6pm. Sat/Sun limited availability.

Colors: Burgundy, teal, jewel tones, incorporate leopard print

Target Market(s)

Moms and grandmas ages 18 to 70.

Industry/Entity Type

Boutique

Font styles to use
Decorative
Script

Requirements
Must have
• The size of the banner is 801X250.
• Company Name: Brimwell Lane Buy Group
• Overall Theme: Want to include crosses somehow, make it girly, flowers, vintage, professional
• We need all of the same information on there. I attached a picture of the previous banner. We don’t like it at all so don’t use it as inspiration.
• Information:
• Private Message: Morwen Pike (best way to contact) <- please make “(best way to contact)” small
• Email: morwenpike@brimwelllane.com
• Emails and private messages are answered weekdays 8am to 6pm. Sat/Sun limited availability.
• Colors: Burgundy, teal, jewel tones, incorporate leopard print

```html
<!DOCTYPE html>
<html lang="en">
<head>
<meta charset="utf-8">
<title>Brimwell Lane Buy Group – Group Banner</title>
<link rel="stylesheet" href="https://fonts.googleapis.com/css2?family=Great+Vibes&family=Roboto+Condensed:wght@300;400;700&display=swap">
<style>
  :root {
    --page: #ffffff;
    --burgundy: #4a1326;
    --burgundy-deep: #300915;
    --burgundy-light: #5c1d33;
    --teal: #0aa6a6;
    --teal-line: #3e8f96;
    --gold: #f7a81b;
    --ink: #4a1326;
    --black: #111111;
    --white: #ffffff;
    --accent-orange: #e8742a;
    --leopard-light: #b8782f;
    --leopard-dark: #6a3814;
    --cross: #1a0a0e;
  }
  * { box-sizing: border-box; margin: 0; padding: 0; }
  html, body {
    width: 1200px; height: 1200px; overflow: hidden;
    background: var(--page);
  }
  .canvas { position: relative; width: 1200px; height: 1200px; }
  .banner {
    position: absolute; left: 0; top: 442px;
    width: 1200px; height: 378px; overflow: hidden;
  }
  .banner-shapes { position: absolute; inset: 0; }

  .group-name {
    position: absolute; left: 640px; top: 72px; width: 400px;
    text-align: center;
    font-family: "Roboto Condensed", sans-serif;
    font-weight: 700; color: var(--white);
    text-transform: uppercase; letter-spacing: 2px; line-height: 1;
  }
  .group-name .line-main { display: block; font-size: 54px; }
  .group-name .line-sub { display: block; font-size: 50px; margin-top: 14px; letter-spacing: 3px; }

  .contact {
    position: absolute; left: 350px; top: 238px; width: 270px;
    text-align: center; color: var(--black);
  }
  .contact-name {
    font-family: "Great Vibes", cursive;
    font-size: 48px; line-height: 1;
  }
  .contact-note {
    font-family: "Roboto Condensed", sans-serif;
    font-weight: 300; font-size: 15px; margin-top: 6px;
  }
  .contact-email {
    font-family: "Roboto Condensed", sans-serif;
    font-weight: 700; font-size: 16px; color: var(--white);
    margin-top: 16px; white-space: nowrap;
  }

  .hours {
    position: absolute; left: 656px; top: 310px;
    font-family: "Roboto Condensed", sans-serif;
    font-size: 18px; color: var(--ink); line-height: 1.3;
    white-space: nowrap;
  }
  .hours-lead { font-weight: 400; letter-spacing: 0.3px; }
  .hours-days { text-transform: uppercase; }
  .hours-sep { display: inline-block; margin: 0 20px; }
</style>
</head>
<body>
<main class="canvas">
  <section class="banner" aria-label="Brimwell Lane Buy Group banner">
    <svg class="banner-shapes" width="1200" height="378" viewBox="0 0 1200 378" xmlns="http://www.w3.org/2000/svg">
      <defs>
        <linearGradient id="photo-field" x1="0" y1="0" x2="0" y2="1">
          <stop offset="0" stop-color="#eac78c"/>
          <stop offset="0.3" stop-color="#8c6b45"/>
          <stop offset="1" stop-color="#5a3b25"/>
        </linearGradient>
        <linearGradient id="photo-smile" x1="0" y1="0" x2="1" y2="1">
          <stop offset="0" stop-color="#d9693a"/>
          <stop offset="1" stop-color="#3a2a26"/>
        </linearGradient>
        <linearGradient id="photo-sisters" x1="0" y1="0" x2="0" y2="1">
          <stop offset="0" stop-color="#6f8a5a"/>
          <stop offset="0.5" stop-color="#d9457a"/>
          <stop offset="1" stop-color="#b9b3ad"/>
        </linearGradient>
        <radialGradient id="burgundy-glow" cx="0.5" cy="0.35" r="0.8">
          <stop offset="0" stop-color="var(--burgundy-light)"/>
          <stop offset="1" stop-color="var(--burgundy-deep)"/>
        </radialGradient>
        <linearGradient id="leopard" x1="0" y1="0" x2="1" y2="1">
          <stop offset="0" stop-color="var(--leopard-light)"/>
          <stop offset="1" stop-color="var(--leopard-dark)"/>
        </linearGradient>
      </defs>

      <!-- photo collage -->
      <rect class="photo photo-field" x="0" y="0" width="242" height="378" fill="url(#photo-field)" role="img" aria-label="Photo of a toddler in a boutique outfit standing in autumn leaves at sunset"/>
      <rect class="divider" x="242" y="0" width="8" height="378" fill="var(--teal)"/>
      <rect class="photo photo-smile" x="250" y="0" width="190" height="198" fill="url(#photo-smile)" role="img" aria-label="Photo of a smiling little girl wearing a striped hair bow"/>
      <rect class="divider" x="250" y="198" width="190" height="6" fill="var(--teal)"/>
      <rect class="photo photo-sisters" x="250" y="204" width="86" height="174" fill="url(#photo-sisters)" role="img" aria-label="Photo of two sisters in matching pink outfits"/>
      <rect class="divider" x="336" y="204" width="4" height="174" fill="var(--teal)"/>
      <rect class="photo photo-dark" x="340" y="204" width="60" height="174" fill="#2e2220" role="img" aria-label="Photo of boutique clothing"/>

      <!-- burgundy field with curved edge -->
      <path class="field" d="M352,0 C405,40 440,110 448,200 L448,378 L1200,378 L1200,0 Z" fill="url(#burgundy-glow)"/>
      <path class="edge-white" d="M352,0 C405,40 440,110 448,200" fill="none" stroke="var(--white)" stroke-width="12"/>
      <path class="edge-teal" d="M362,-2 C415,40 450,110 458,200" fill="none" stroke="var(--teal-line)" stroke-width="4"/>

      <!-- leopard corner -->
      <polygon class="leopard" points="1100,22 1200,22 1200,378 1160,378 1132,328" fill="url(#leopard)" role="img" aria-label="Leopard print panel"/>
      <polygon class="corner-teal" points="1088,0 1200,0 1200,22 1100,22" fill="var(--teal)"/>

      <!-- cross -->
      <rect class="cross" x="1082" y="188" width="9" height="102" fill="var(--cross)"/>
      <rect class="cross" x="1054" y="220" width="72" height="9" fill="var(--cross)" transform="rotate(-10 1090 224)"/>

      <!-- hours band -->
      <polygon class="hours-band" points="560,290 1132,290 1170,338 1200,338 1200,378 560,378" fill="var(--gold)"/>

      <!-- contact badge -->
      <circle cx="482" cy="270" r="150" fill="var(--white)"/>
      <circle cx="482" cy="270" r="146" fill="none" stroke="var(--teal-line)" stroke-width="4"/>
      <path d="M344,306 A140,140 0 0 0 352,336" fill="none" stroke="var(--accent-orange)" stroke-width="4"/>
      <circle cx="482" cy="270" r="136" fill="var(--teal)"/>
    </svg>

    <h1 class="group-name">
      <span class="line-main">Brimwell Lane</span>
      <span class="line-sub">Buy Group</span>
    </h1>

    <div class="contact">
      <p class="contact-name">Morwen Pike</p>
      <p class="contact-note">(BEST WAY TO CONTACT)</p>
      <p class="contact-email">morwenpike@brimwelllane.com</p>
    </div>

    <div class="hours">
      <p class="hours-lead">Emails and private messages are answered</p>
      <p class="hours-days">Weekdays 8am to 6pm<span class="hours-sep">|</span>Sat/Sun limited availability.</p>
    </div>
  </section>
</main>
</body>
</html>
```